New, modern business card for growing audiology practice

We need a new business card for our audiology practice. Our logo and website have recently changed (more modern) and we want our business cards to reflect this change.
We conduct hearing tests, perform earwax removals, and fit & dispense hearing aids to our patients. We are a family owned practice in which the owner is the one who works directly with the patient. I have attached logos in various formats to use, as well as two ideas I found on this website; as well as a scanned copy of our current logo. Good luck!

Industry/Entity Type

Business

Contact Information for Business Card

Company name: Maplow Hearing Center
Provider name: Peter Mulvoy, Au.D. F/ISN
Phone number: (555) 318-6042
Address: 87 W. Linden Ave. Ashcombe, OH 44099
email: maplowhearing@postvale.net
website: maplowhearing.com

Colors
000000
aaaaaa
dbdbdb
cacaca
9bcb3c
afd23c
cadf82
b1b1b1

Requirements
Must have
• My card must include information in the "details" section. In the attached images, I found a few that I liked and I would like to model after - "brisk tumblin'" and "Sound Wellness Center".
• Must be horizontal.
• Must include logos provided. I uploaded them in various file formats and various ways.
• Must match logo font, if possible, if not, please get as close as you can.
Nice to have
• I really like the idea of having a color on one side with just the logo and company name and the contact information and provider name on the other side. I also really like the idea of having the main color dominating on the logo/company side with accent of that same color on the contact side of the card.
Should not have
• Must not be vertical.

```html
<!DOCTYPE html>
<html lang="en">
<head>
<meta charset="utf-8">
<title>Maplow Hearing Center – Business Card</title>
<link rel="stylesheet" href="https://fonts.googleapis.com/css2?family=Roboto:wght@400;500;700&display=swap">
<style>
  :root {
    --bg: #e6e6e4;
    --green-light: #9bcb3c;
    --green-mid: #6fb23a;
    --green-deep: #4c8f2a;
    --accent: #6aa83a;
    --ink: #1d1d1d;
    --ink-soft: #333333;
    --paper: #ffffff;
    --shadow: rgba(0, 0, 0, 0.18);
  }
  * { margin: 0; padding: 0; box-sizing: border-box; }
  html, body {
    width: 1200px;
    height: 913px;
    overflow: hidden;
    background: var(--bg);
    font-family: "Roboto", Arial, sans-serif;
  }
  .sheet {
    width: 1200px;
    height: 913px;
    display: flex;
    align-items: center;
    justify-content: center;
    gap: 40px;
  }
  .card {
    width: 520px;
    height: 297px;
    border-radius: 4px;
    box-shadow: 0 10px 24px var(--shadow);
    position: relative;
    overflow: hidden;
  }
  /* Front side */
  .card--front {
    background: linear-gradient(160deg, var(--green-light) 0%, var(--green-mid) 45%, var(--green-deep) 100%);
    display: flex;
    align-items: center;
    justify-content: center;
  }
  .brand {
    display: flex;
    align-items: center;
    gap: 14px;
  }
  .brand__dot {
    width: 18px;
    height: 18px;
    border-radius: 50%;
    flex: none;
  }
  .brand__name {
    font-weight: 400;
    text-transform: uppercase;
    line-height: 1.05;
  }
  .card--front .brand__dot { background: var(--paper); }
  .card--front .brand__name {
    color: var(--paper);
    font-size: 34px;
    letter-spacing: 0.5px;
  }
  /* Back side */
  .card--back { background: var(--paper); }
  .card--back .brand {
    position: absolute;
    right: 34px;
    top: 120px;
  }
  .card--back .brand__dot { background: var(--accent); width: 14px; height: 14px; }
  .card--back .brand__name {
    color: var(--ink);
    font-size: 21px;
  }
  .provider {
    position: absolute;
    left: 34px;
    top: 70px;
  }
  .provider__name {
    color: var(--accent);
    font-weight: 700;
    font-size: 17px;
  }
  .provider__role {
    color: var(--ink-soft);
    font-weight: 500;
    font-size: 11px;
    margin-top: 6px;
  }
  .contact {
    position: absolute;
    left: 34px;
    bottom: 40px;
    list-style: none;
    font-size: 12px;
    font-weight: 500;
    color: var(--ink);
  }
  .contact__item {
    display: flex;
    align-items: flex-start;
    gap: 10px;
    line-height: 1.35;
  }
  .contact__icon {
    width: 12px;
    height: 12px;
    flex: none;
    margin-top: 2px;
    fill: var(--accent);
  }
</style>
</head>
<body>
<main class="sheet">
  <section class="card card--front" aria-label="Card front">
    <div class="brand">
      <span class="brand__dot"></span>
      <span class="brand__name">Maplow<br>Hearing Center</span>
    </div>
  </section>

  <section class="card card--back" aria-label="Card back">
    <div class="provider">
      <p class="provider__name">Peter Mulvoy, Au.D. F/ISN</p>
      <p class="provider__role">Owner - Audiologist</p>
    </div>

    <div class="brand">
      <span class="brand__dot"></span>
      <span class="brand__name">Maplow<br>Hearing Center</span>
    </div>

    <ul class="contact">
      <li class="contact__item">
        <svg class="contact__icon" viewBox="0 0 24 24" aria-hidden="true"><path d="M12 2a7 7 0 0 0-7 7c0 5 7 13 7 13s7-8 7-13a7 7 0 0 0-7-7zm0 9.5A2.5 2.5 0 1 1 12 6.5a2.5 2.5 0 0 1 0 5z"/></svg>
        <span>87 W. Linden Ave.<br>Ashcombe, OH 44099</span>
      </li>
      <li class="contact__item">
        <svg class="contact__icon" viewBox="0 0 24 24" aria-hidden="true"><path d="M6.6 10.8a15 15 0 0 0 6.6 6.6l2.2-2.2a1 1 0 0 1 1-.25 11.4 11.4 0 0 0 3.6.57 1 1 0 0 1 1 1V20a1 1 0 0 1-1 1A17 17 0 0 1 3 4a1 1 0 0 1 1-1h3.5a1 1 0 0 1 1 1c0 1.25.2 2.45.57 3.6a1 1 0 0 1-.25 1z"/></svg>
        <span>(555) 318-6042</span>
      </li>
      <li class="contact__item">
        <svg class="contact__icon" viewBox="0 0 24 24" aria-hidden="true"><path d="M2 5h20v14H2zm2 2v.5l8 5 8-5V7l-8 5z"/></svg>
        <span>maplowhearing@postvale.net</span>
      </li>
      <li class="contact__item">
        <svg class="contact__icon" viewBox="0 0 24 24" aria-hidden="true"><path d="M12 2a10 10 0 1 0 0 20 10 10 0 0 0 0-20zm6.9 9h-3a15 15 0 0 0-1.3-5.6A8 8 0 0 1 18.9 11zM12 4.1c.9 1.2 1.8 3.6 1.9 6.9h-3.8c.1-3.3 1-5.7 1.9-6.9zM9.4 5.4A15 15 0 0 0 8.1 11h-3a8 8 0 0 1 4.3-5.6zM5.1 13h3a15 15 0 0 0 1.3 5.6A8 8 0 0 1 5.1 13zm6.9 6.9c-.9-1.2-1.8-3.6-1.9-6.9h3.8c-.1 3.3-1 5.7-1.9 6.9zm2.6-1.3a15 15 0 0 0 1.3-5.6h3a8 8 0 0 1-4.3 5.6z"/></svg>
        <span>www.maplowhearing.com</span>
      </li>
    </ul>
  </section>
</main>
</body>
</html>
```